Build Distinctive Business Card: Public Relations Government Relations firm

I have logo and colors done (attached) need a very cool way to present it on a business card (can be two sided if need be).

Public Relations Government Relations firm

Info:

Mark Tillson, CEO
Keystone Public Relations
2786 West Harlow Blvd.
Los Angeles CA 90047
(o) 213.555.0148
(f) 213.555.0193
mark@keystonekpr-example.com

Target Market(s)

Government relations, public relations, lobbyist, I was a past State Senator

Industry/Entity Type

Business

Contact Information for Business Card

Info:

Mark Tillson, CEO
Keystone Public Relations
2786 West Harlow Blvd.
Los Angeles CA 90047
(o) 213.555.0148
(f) 213.555.0193
mark@keystonekpr-example.com
@marktillson

Requirements
Must have
• A sense of balance given logo is already done.
• It's a government relations firm really.
• Lobbyist type.
• Senatorial type...

```html
<!DOCTYPE html>
<html lang="en">
<head>
<meta charset="utf-8">
<title>Keystone Public Relations – Business Card</title>
<link href="https://fonts.googleapis.com/css2?family=Open+Sans:wght@400;600&display=swap" rel="stylesheet">
<style>
  :root {
    --backdrop: #2e2f31;
    --paper: #f7f8f8;
    --paper-edge: #dcdfe0;
    --brand-blue: #0f74a8;
    --brand-blue-dark: #0a5c88;
    --ink-blue: #2f86bd;
    --ink-grey: #5c6266;
    --rule-grey: #c9cdd0;
  }
  * { margin: 0; padding: 0; box-sizing: border-box; }
  html, body {
    width: 1200px;
    height: 900px;
    overflow: hidden;
    background: var(--backdrop);
    font-family: "Open Sans", Arial, sans-serif;
  }
  .canvas {
    position: relative;
    width: 1200px;
    height: 900px;
  }
  .card {
    position: absolute;
    width: 525px;
    height: 300px;
    background: var(--paper);
    box-shadow: 0 2px 0 var(--paper-edge), 0 14px 30px rgba(0,0,0,0.45);
    overflow: hidden;
  }

  /* Contact side */
  .card-contact {
    left: 55px;
    top: 150px;
    display: flex;
    align-items: center;
  }
  .identity {
    width: 205px;
    text-align: right;
    padding-right: 22px;
  }
  .person-name {
    color: var(--ink-blue);
    font-size: 17px;
    font-weight: 600;
    letter-spacing: 0.5px;
  }
  .person-title {
    color: var(--ink-grey);
    font-size: 12px;
    margin-top: 2px;
  }
  .divider {
    width: 1px;
    height: 96px;
    background: var(--rule-grey);
  }
  .contact-list {
    list-style: none;
    padding-left: 18px;
    color: var(--ink-grey);
    font-size: 11px;
    line-height: 17px;
  }
  .contact-list li {
    display: flex;
    align-items: flex-start;
    gap: 7px;
  }
  .contact-list svg {
    width: 11px;
    height: 11px;
    margin-top: 3px;
    flex: none;
    fill: var(--ink-grey);
  }
  .contact-list .indent { padding-left: 18px; }

  /* Brand side */
  .card-brand {
    left: 620px;
    top: 450px;
    display: flex;
    flex-direction: column;
  }
  .band {
    height: 66px;
    background: linear-gradient(180deg, var(--brand-blue) 0%, var(--brand-blue-dark) 100%);
  }
  .brand-field {
    flex: 1;
    display: flex;
    align-items: center;
    justify-content: center;
    gap: 18px;
    background: linear-gradient(180deg, #ffffff 0%, #eef1f2 100%);
  }
  .brand-dot {
    width: 74px;
    height: 74px;
    border-radius: 50%;
    background: var(--brand-blue);
  }
  .brand-name {
    color: var(--brand-blue);
    font-size: 50px;
    font-weight: 600;
    letter-spacing: -0.5px;
  }
</style>
</head>
<body>
<main class="canvas">

  <section class="card card-contact" aria-label="Contact side">
    <div class="identity">
      <p class="person-name">Mark Tillson</p>
      <p class="person-title">CEO</p>
    </div>
    <div class="divider"></div>
    <ul class="contact-list">
      <li>
        <svg viewBox="0 0 12 12" aria-hidden="true"><path d="M2.5 1h2l1 2.6-1.3 1a6 6 0 0 0 2.6 2.6l1-1.3 2.7 1v2A1.2 1.2 0 0 1 9.3 11 8.5 8.5 0 0 1 1 2.7 1.2 1.2 0 0 1 2.5 1z"/></svg>
        213.555.0148
      </li>
      <li>
        <svg viewBox="0 0 12 12" aria-hidden="true"><path d="M1 1h10v10H1z M2.5 2.5v7h7v-7z"/></svg>
        213.555.0193
      </li>
      <li>
        <svg viewBox="0 0 12 12" aria-hidden="true"><path d="M0.5 2.5h11v7h-11z M1.5 3.3v.5L6 6.8l4.5-3v-.5L6 6z" fill-rule="evenodd"/></svg>
        mark@keystonekpr-example.com
      </li>
      <li>
        <svg viewBox="0 0 12 12" aria-hidden="true"><path d="M6 1 11 5.5H9.5V11h-2.5V7.8H5V11H2.5V5.5H1z"/></svg>
        Keystone Public Relations
      </li>
      <li class="indent">2786 West Harlow Blvd.</li>
      <li class="indent">Los Angeles CA 90047</li>
    </ul>
  </section>

  <section class="card card-brand" aria-label="Brand side">
    <div class="band"></div>
    <div class="brand-field">
      <div class="brand-dot"></div>
      <span class="brand-name">Keystone</span>
    </div>
    <div class="band"></div>
  </section>

</main>
</body>
</html>
```